Email signature design - law firm

We are a small boutique law firm which is located near the beach in Manly, Australia.

We have just recently developed a new logo and are looking to redesign our letterhead, business cards and email signatures.

This brief is for our email signatures. This is an email signature to appear at the bottom of our Outlook emails so we would like it to be text that we are able to edit as the wording in our email signature often required amendments.

I have attached a word document which had our new logo, and our previous email signature which all the information/wording that needs to be included.

We would like multiple designs with a modern, simplistic yet striking look.

Thanks.

font - raleway or montserrat
Updates

Colors

Designer to choose colors to be used in the design.

Requirements
Must have
• Must have the exact wording which appears in the email signature in the word document attached to brief.
• Must be able to edit the text as it is for an Outlook email signature which wording will change from time to time.

```html
<!DOCTYPE html>
<html lang="en">
<head>
<meta charset="utf-8">
<title>Email Signature – Harbourlee Lawyers</title>
<link rel="stylesheet" href="https://fonts.googleapis.com/css2?family=Raleway:wght@600;700&family=Lato:wght@400;700&display=swap">
<style>
  :root {
    --page-bg: #f2f2f2;
    --card-bg: #ffffff;
    --band: #6678b4;
    --name-ink: #e3e8f8;
    --ink: #1d1d1f;
    --icon: #2e3a7a;
    --band-text: #ffffff;
    --brand-ink: #1f2230;
  }
  * { margin: 0; padding: 0; box-sizing: border-box; }
  html, body {
    width: 1200px; height: 757px; overflow: hidden;
    background: var(--page-bg);
  }
  .signature {
    position: absolute;
    left: 316px; top: 363px;
    width: 570px; height: 131px;
    background: var(--card-bg);
    font-family: "Lato", Arial, sans-serif;
    color: var(--ink);
  }
  .signature__bands { position: absolute; inset: 0; }
  .signature__name {
    position: absolute; left: 30px; top: 6px;
    font-family: "Raleway", Arial, sans-serif;
    font-weight: 700; font-size: 17.5px; letter-spacing: 0.2px;
    color: var(--name-ink);
    white-space: nowrap;
  }
  .signature__role {
    font-family: "Lato", Arial, sans-serif;
    font-weight: 400; font-size: 13px; letter-spacing: 0;
    color: var(--ink); margin-left: 4px;
  }
  .contact {
    position: absolute; left: 29px;
    display: flex; align-items: center; gap: 8px;
    font-size: 13.5px; white-space: nowrap;
  }
  .contact--phone { top: 52px; }
  .contact--email { top: 77px; }
  .contact__icon { width: 16px; height: 14px; fill: var(--icon); }
  .signature__web {
    position: absolute; left: 30px; top: 110px;
    font-weight: 700; font-size: 13px;
    color: var(--band-text);
  }
  .brand {
    position: absolute; left: 400px; top: 0; width: 170px; height: 131px;
    display: flex; align-items: center; justify-content: center; gap: 8px;
  }
  .brand__mark { width: 12px; height: 12px; border-radius: 50%; background: var(--band); }
  .brand__name {
    font-family: "Raleway", Arial, sans-serif;
    font-weight: 700; font-size: 15px; color: var(--brand-ink);
    letter-spacing: 0.4px;
  }
</style>
</head>
<body>
  <div class="signature">
    <svg class="signature__bands" width="570" height="131" viewBox="0 0 570 131" aria-hidden="true">
      <polygon points="0,0 378,0 346,32 0,32" fill="var(--band)"/>
      <polygon points="0,107 350,107 393,131 0,131" fill="var(--band)"/>
    </svg>

    <div class="signature__name">NORA ELLISON <span class="signature__role">Practise Manager</span></div>

    <div class="contact contact--phone">
      <svg class="contact__icon" viewBox="0 0 16 14" aria-hidden="true">
        <path d="M1 3.5C1 1.5 4 1 8 1s7 .5 7 2.5V5h-3.5V3.8H4.5V5H1z"/>
        <path d="M4 6h8l2.5 7h-13z M8 7.6a2 2 0 1 0 0 4 2 2 0 1 0 0-4z"/>
      </svg>
      <span>(021) 4830 1174</span>
    </div>

    <div class="contact contact--email">
      <svg class="contact__icon" viewBox="0 0 16 14" aria-hidden="true">
        <path d="M0 1.5h16v11H0z M1.5 3v8h13V3L8 8z" fill-rule="evenodd"/>
        <path d="M1.6 2.8h12.8L8 7.6z"/>
      </svg>
      <span>nora.ellison@harbourleelaw.com.au</span>
    </div>

    <div class="signature__web">www.harbourleelaw.com.au</div>

    <div class="brand">
      <span class="brand__mark"></span>
      <span class="brand__name">Harbourlee Lawyers</span>
    </div>
  </div>
</body>
</html>
```